Flyer-Design für Business Center
Zielgruppe
Wir sind Co-Working /Business Center Anbieter auf Basis eines Mitgliedschaft Konzeptes. Bei uns kann man Arbeitsplätze und Büroräume mit Kaffee und Wasser in einer Lounge anmieten. Dazu bieten wir Bedarfsgerechte Mitgliedschaften an. Unsere Kunden sind Kreative, Programmierer, Freiberufler aber auch größere Unternehmen.
Aufgabenstellung
DIN LANG A 4, der Flyer wird gedruckt und kommt in Aussteller. Er soll als Eye Catcher den Preis ab 69,90 für 4 Wochen beinhalten. In diesem Preis ist alles inclusive. Also Wasser, Kaffee, Cappuccino, Drucker, Kopierer, Möbel, Putzfrau, Schreibtisch. Bürostuhl. Gleichzeitig soll der Flyer auch als PDF versendet werden können.
Weitere Information findet man auf unserer Webseite www.kranichfeldwerk.com

```html
<!DOCTYPE html>
<html lang="de">
<head>
<meta charset="utf-8">
<title>Kranichfeld Werk – Flyer DIN lang</title>
<link href="https://fonts.googleapis.com/css2?family=Open+Sans:wght@300;400;700&display=swap" rel="stylesheet">
<style>
  :root{
    --blue:#139fd3;
    --grey:#9d9d9d;
    --head-grey:#8a8a8a;
    --text-grey:#a3a3a3;
    --panel-light:#f4f4f4;
    --white:#ffffff;
  }
  *{box-sizing:border-box;margin:0;padding:0}
  html,body{width:1200px;height:900px;overflow:hidden;background:var(--white)}
  body{position:relative;font-family:"Open Sans",Arial,sans-serif}
  .flyer{position:absolute;top:57px;width:393px;height:786px;background:var(--white);
    box-shadow:4px 6px 10px rgba(0,0,0,.18);overflow:hidden}
  .flyer--front{left:200px}
  .flyer--back{left:626px}
  .band{position:absolute;left:0;width:100%}
  .band--split{height:20px;background:linear-gradient(90deg,var(--grey) 50%,var(--blue) 50%)}
  .band--top{top:0}
  .band--bottom{top:766px}

  /* front */
  .brand-area{position:absolute;top:20px;left:0;width:100%;height:173px;background:var(--panel-light);
    display:flex;flex-direction:column;align-items:center;justify-content:center;gap:10px}
  .brand-mark{width:30px;height:30px;border-radius:50%;background:var(--blue)}
  .brand-name{font-weight:400;color:var(--blue);font-size:30px;line-height:1.1;text-align:center;letter-spacing:.5px}
  .contact-bar{position:absolute;top:193px;height:19px;width:100%;background:var(--blue);color:var(--white);
    font-size:8.6px;font-weight:700;text-align:center;line-height:19px;white-space:nowrap}
  .headline{position:absolute;top:212px;height:56px;width:100%;text-align:center;font-weight:700;
    font-size:41px;line-height:56px;color:var(--head-grey);letter-spacing:.5px}
  .headline .accent{color:var(--blue)}
  .band--blue{top:268px;height:19px;background:var(--blue)}
  .photo{position:absolute;top:287px;left:0;width:100%;height:305px;
    background:radial-gradient(circle at 52% 45%,#d7cfc7 0%,#c9c0b8 45%,#b7aea6 100%)}
  .band--grey{top:592px;height:19px;background:var(--grey)}
  .price-badge{position:absolute;left:109px;top:492px;width:174px;height:200px}
  .price-text{position:absolute;left:109px;top:540px;width:174px;text-align:center;color:var(--white)}
  .price-text .amount{font-weight:700;font-size:37px;line-height:1.1}
  .price-text .period{font-weight:400;font-size:16px;line-height:1.3}
  .includes{position:absolute;top:690px;width:100%;text-align:center}
  .includes h3{color:var(--blue);font-weight:700;font-size:16.5px;line-height:1.3}
  .includes p{color:var(--text-grey);font-weight:300;font-size:11.8px;line-height:17.5px;margin-top:1px}

  /* back */
  .section{position:absolute;left:30px;width:332px}
  .section h2{color:var(--blue);font-weight:700;font-size:16.5px;line-height:1.2}
  .section p{color:var(--text-grey);font-weight:300;font-size:11.4px;line-height:17.5px;text-align:justify;margin-top:10px}
  .about{top:38px}
  .services{position:absolute;top:191px;left:0;width:100%;height:340px;background:var(--blue)}
  .service{position:absolute;left:30px;width:337px;display:flex}
  .service-icon{flex:0 0 82px;width:82px;height:82px;border-radius:50%;background:var(--white);
    display:flex;align-items:center;justify-content:center;margin-right:11px}
  .service-body h3{color:var(--white);font-weight:700;font-size:16.5px;line-height:1.2}
  .service-body p{color:var(--white);font-weight:300;font-size:11.4px;line-height:17.5px;text-align:justify;margin-top:2px}
  .service--cowork{top:20px}
  .service--office{top:132px}
  .service--address{top:235px}
  .locations{top:551px}
  .locations p{margin-top:18px}
  .location-list{position:absolute;left:30px;top:721px;display:flex;align-items:center;gap:8px;
    color:var(--blue);font-weight:700;font-size:11.6px}
</style>
</head>
<body>

<article class="flyer flyer--front">
  <div class="band band--split band--top"></div>
  <header class="brand-area">
    <div class="brand-mark"></div>
    <div class="brand-name">Kranichfeld<br>Werk</div>
  </header>
  <div class="contact-bar">Tel.: +49-228-555019-00 · info@kranichfeldwerk.com · www.kranichfeldwerk.com</div>
  <h1 class="headline">KEIN <span class="accent">BÜRO?</span></h1>
  <div class="band band--blue"></div>
  <div class="photo" role="img" aria-label="Foto: fröhlicher Hund sitzt zwischen zerrissenem Papier auf hellem Holzboden"></div>
  <div class="band band--grey"></div>
  <svg class="price-badge" viewBox="0 0 174 200" aria-hidden="true">
    <path d="M87 0 A84 84 0 0 1 140 149 L87 198 L34 149 A84 84 0 0 1 87 0 Z" fill="#139fd3"/>
    <circle cx="87" cy="84" r="71" fill="none" stroke="#ffffff" stroke-width="2"/>
  </svg>
  <div class="price-text">
    <div class="amount">69,90€</div>
    <div class="period">für 4 Wochen</div>
  </div>
  <section class="includes">
    <h3>inklusive</h3>
    <p>Wasser, Kaffee, Cappuccino, Drucker, Kopierer, Möbel,<br>Putzfrau, Schreibtisch &amp;Bürostuhl</p>
  </section>
  <div class="band band--split band--bottom"></div>
</article>

<article class="flyer flyer--back">
  <div class="band band--split band--top"></div>
  <section class="section about">
    <h2>Über Kranichfeld Werk</h2>
    <p>Als neues Unternehmen im Bereich Co-Working und Business Center verfügt unser Team dennoch über lange Erfahrung und zahlreiche Erfolgsgeschichten zurück. Unsere Mission besteht darin, Büroraum effizient und günstig nutzbar sowie zugänglich zu machen. Mit unseren Membership Konzept können User direkt durchstarten. Dabei behalten sie die notwendige Flexibilität.</p>
  </section>

  <section class="services">
    <div class="service service--cowork">
      <div class="service-icon">
        <svg width="54" height="58" viewBox="0 0 54 58" fill="none" stroke="#139fd3" stroke-width="4" stroke-linejoin="round">
          <circle cx="19" cy="9" r="6"/><circle cx="36" cy="13" r="5"/>
          <path d="M10 28 Q12 16 19 16 Q26 16 28 28"/><path d="M29 28 Q30 20 36 20 Q42 20 43 28"/>
          <rect x="4" y="28" width="46" height="9" rx="4"/><rect x="9" y="37" width="36" height="17"/>
        </svg>
      </div>
      <div class="service-body">
        <h3>Coworking</h3>
        <p>Nutze flexible einen oder mehrer Arbeitplätze in allen Centen. In deinen Heimatcenter kannst du einen Platz reservieren, der nur für dich da ist.</p>
      </div>
    </div>
    <div class="service service--office">
      <div class="service-icon">
        <svg width="54" height="58" viewBox="0 0 54 58" fill="none" stroke="#139fd3" stroke-width="4" stroke-linejoin="round">
          <circle cx="27" cy="9" r="6"/><path d="M18 28 Q19 16 27 16 Q35 16 36 28"/>
          <rect x="4" y="28" width="46" height="9" rx="4"/><rect x="9" y="37" width="36" height="17"/>
        </svg>
      </div>
      <div class="service-body">
        <h3>Büros</h3>
        <p>Private Büros stehen dir bei Bedarf oder auch ständig zur Verfügung. Von einen Arbeitsplatz bis sechs Arbeitsplätze.</p>
      </div>
    </div>
    <div class="service service--address">
      <div class="service-icon">
        <svg width="52" height="36" viewBox="0 0 52 36" fill="none" stroke="#139fd3" stroke-width="4" stroke-linejoin="round">
          <rect x="3" y="3" width="46" height="30"/><path d="M3 3 Q26 30 49 3"/><path d="M3 33 L16 22 M49 33 L36 22"/>
        </svg>
      </div>
      <div class="service-body">
        <h3>Geschäftsadresse</h3>
        <p>Einfach nur Post ankommen und bearbeiten lassen. Die Geschäftsadresse bietet dir Platz im eigenen Briefkasten und lässt dich auf deine Webseite professionell aussehn.</p>
      </div>
    </div>
  </section>

  <section class="section locations">
    <h2>Standorte</h2>
    <p>Alle unsere Standorte befinden sich in idealer Lage für dein Geschäft. Wir achten sehr darauf, dass du verkehrsgünstig zu deinem neuen Büro kommen kannst. Dabei ist es egal ob mit dem Auto oder mit öffentlichen Verkehrsmitteln. Fühle dich in unseren Center wohler als in einem anderen Büro. Unsere Lounge versorgt dich kostenfrei mit Kaffee, Wasser, Cappuccino und Tee.</p>
  </section>
  <div class="location-list">
    <svg width="20" height="26" viewBox="0 0 20 26" aria-hidden="true">
      <path d="M10 0 A10 10 0 0 1 20 10 C20 17 10 26 10 26 C10 26 0 17 0 10 A10 10 0 0 1 10 0 Z" fill="#139fd3"/>
      <circle cx="10" cy="10" r="4" fill="#ffffff"/>
    </svg>
    <span>Monheim am Rhein, Frankfurt am Rhein, Berlin, Bonn</span>
  </div>
  <div class="band band--split band--bottom"></div>
</article>

</body>
</html>
```